Maple Crest

We have opened new business that includes pottery & chimineas we want cards to have collage of pictures of products on front of card then information on back. On back in middle MAPLE CREST +
marla_fenwick@quillmail.net
(555) 218-0347
(555)2180392 & maplecrest@quillmail.net
Industry/Entity Type
Business
Font styles to use
Sans Serif
Decorative

```html
<!DOCTYPE html>
<html lang="en">
<head>
<meta charset="utf-8">
<title>Maple Crest – Business Cards</title>
<link rel="stylesheet" href="https://fonts.googleapis.com/css2?family=Arimo:wght@400;700&family=Great+Vibes&display=swap">
<style>
  :root {
    --page: #ffffff;
    --card-shadow: rgba(0, 0, 0, 0.45);
    --title-fill-top: #ffffff;
    --title-fill-bottom: #b9d3da;
    --title-stroke: #1f3a44;
    --back-title-fill: #2a2e30;
    --back-title-stroke: #8fb3bf;
    --script-ink: #111111;
    --script-light: #ffffff;
    --contact-ink: #ffffff;
    --ceramic-green: #7b7a3a;
    --ceramic-blue: #3f5a63;
    --ceramic-brown: #6e4b32;
    --ceramic-sand: #c9b89a;
    --clay-dark: #1a1a1a;
    --clay-mid: #6b6b6b;
    --clay-light: #d8d8d8;
  }
  html, body {
    margin: 0;
    padding: 0;
    width: 1175px;
    height: 1200px;
    overflow: hidden;
    background: var(--page);
  }
  .canvas {
    position: relative;
    width: 1175px;
    height: 1200px;
  }
  .card {
    position: absolute;
    width: 874px;
    height: 490px;
    overflow: hidden;
    box-shadow: 10px 12px 14px var(--card-shadow);
  }
  .card--front { left: 141px; top: 51px; }
  .card--back  { left: 150px; top: 634px; background: var(--clay-dark); }

  .photo {
    position: absolute;
    inset: 0;
  }
  .photo--products {
    background:
      radial-gradient(ellipse 22% 40% at 14% 60%, var(--ceramic-blue) 0%, transparent 70%),
      radial-gradient(ellipse 18% 45% at 42% 55%, var(--ceramic-sand) 0%, transparent 75%),
      radial-gradient(ellipse 16% 50% at 62% 68%, var(--ceramic-green) 0%, transparent 75%),
      radial-gradient(ellipse 16% 45% at 90% 62%, var(--ceramic-blue) 0%, transparent 75%),
      radial-gradient(ellipse 20% 35% at 78% 35%, var(--ceramic-brown) 0%, transparent 75%),
      linear-gradient(180deg, #8f8a78 0%, #5e5a4a 55%, #a39a84 100%);
  }
  .photo--potter {
    background:
      radial-gradient(ellipse 40% 55% at 48% 48%, var(--clay-light) 0%, var(--clay-mid) 45%, transparent 80%),
      radial-gradient(ellipse 30% 40% at 85% 40%, #8a8a8a 0%, transparent 75%),
      linear-gradient(180deg, #2b2b2b 0%, var(--clay-dark) 100%);
  }

  .brand-title {
    position: absolute;
    margin: 0;
    font-family: "Arimo", Arial, sans-serif;
    font-weight: 400;
    letter-spacing: 2px;
    white-space: nowrap;
  }
  .card--front .brand-title {
    left: 0; right: 0;
    top: 26px;
    text-align: center;
    font-size: 106px;
    line-height: 1;
    background: linear-gradient(180deg, var(--title-fill-top) 30%, var(--title-fill-bottom) 100%);
    -webkit-background-clip: text;
    background-clip: text;
    color: transparent;
    -webkit-text-stroke: 2px var(--title-stroke);
  }
  .card--back .brand-title {
    left: 28px;
    top: 16px;
    font-size: 74px;
    line-height: 1;
    color: var(--back-title-fill);
    -webkit-text-stroke: 1.5px var(--back-title-stroke);
  }

  .monogram {
    position: absolute;
    left: 545px;
    top: 185px;
    margin: 0;
    font-family: "Great Vibes", cursive;
    font-size: 150px;
    line-height: 1;
    color: var(--script-ink);
    text-shadow: 0 0 14px rgba(255, 255, 255, 0.9), 0 0 4px rgba(255, 255, 255, 0.9);
  }

  .owner-name {
    position: absolute;
    left: 42px;
    top: 232px;
    margin: 0;
    font-family: "Great Vibes", cursive;
    font-weight: 400;
    font-size: 96px;
    line-height: 1;
    white-space: nowrap;
    color: var(--script-ink);
    transform: rotate(-11deg);
    transform-origin: 0 80%;
    text-shadow:
      0 0 6px var(--script-light),
      0 0 12px var(--script-light),
      0 0 22px var(--script-light);
  }

  .contact {
    position: absolute;
    left: 76px;
    top: 382px;
    display: grid;
    grid-template-columns: 493px auto;
    row-gap: 7px;
    margin: 0;
    font-family: "Arimo", Arial, sans-serif;
    font-size: 29px;
    line-height: 1.2;
    color: var(--contact-ink);
  }
  .contact dd { margin: 0; }
  .contact__phone { font-weight: 700; }
</style>
</head>
<body>
<main class="canvas">

  <section class="card card--front" aria-label="Card front">
    <div class="photo photo--products" role="img" aria-label="Collage of glazed pottery urns, vases, a wrought-iron panel and clay chimineas"></div>
    <h1 class="brand-title">MAPLE CREST</h1>
    <p class="monogram">M</p>
  </section>

  <section class="card card--back" aria-label="Card back">
    <div class="photo photo--potter" role="img" aria-label="Black and white photo of hands shaping clay on a potter's wheel"></div>
    <h2 class="brand-title">MAPLE CREST</h2>
    <p class="owner-name">Dale &amp; marla Fenwick</p>
    <dl class="contact">
      <dd class="contact__email">marla_fenwick@quillmail.net</dd>
      <dd class="contact__phone">(555) 218-0347</dd>
      <dd class="contact__email">maplecrest@quillmail.net</dd>
      <dd class="contact__phone">(555) 218-0392</dd>
    </dl>
  </section>

</main>
</body>
</html>
```